Flyer for IT Support Company

We need a 1 sided A5 flyer to promote our services and support packages to local businesses, I have attached the sort of content and layout we are looking for but happy for you to be creative with backgrounds and colors. It needs to look modern and professional but catch the eye ;-)
The strap-line on the logo needs to be changed to to 'Your Local IT Company'

It Company

```html
<!DOCTYPE html>
<html lang="en">
<head>
<meta charset="utf-8">
<title>Corvanta – Affordable IT Support Packages</title>
<link href="https://fonts.googleapis.com/css2?family=Cabin:wght@400;500;600;700&display=swap" rel="stylesheet">
<style>
  :root{
    --green:#8aa32b;
    --green-dark:#6f8a1d;
    --green-light:#a3b94a;
    --plum:#95145f;
    --plum-dark:#7a0e4d;
    --pink-row:#d9b3cb;
    --pink-row-alt:#e2c3d6;
    --paper:#f3f2f0;
    --stage:#e9e9e9;
    --ink:#3b2a33;
    --white:#ffffff;
    --icon:#3a3a3a;
  }
  *{box-sizing:border-box;margin:0;padding:0}
  html,body{width:1200px;height:1000px;overflow:hidden}
  body{background:var(--stage);font-family:"Cabin",sans-serif;color:var(--ink)}
  .flyer{position:absolute;left:270px;top:30px;width:660px;height:940px;background:var(--paper);overflow:hidden;box-shadow:0 2px 10px rgba(0,0,0,.12)}
  .sketch-bg{position:absolute;right:0;top:215px;width:420px;height:520px;background:radial-gradient(ellipse at 70% 40%,rgba(150,150,150,.22),rgba(150,150,150,0) 70%)}
  .header{position:absolute;left:0;top:0;width:100%;height:215px;background:var(--green)}
  .brand{position:absolute;left:30px;top:26px;display:flex;align-items:center;gap:8px}
  .brand-dot{width:34px;height:34px;border-radius:50%;background:var(--white);opacity:.9}
  .brand-name{font-size:46px;font-weight:700;color:var(--white);line-height:1}
  .strap{position:absolute;left:74px;top:76px;font-size:11px;letter-spacing:2.4px;color:#c9d98f;font-weight:600}
  .badge{position:absolute;right:0;top:0;width:250px;height:92px;background:var(--plum);border:2px solid #c86aa0;border-top:none;border-right:none;border-radius:0 0 0 12px;color:var(--white);font-weight:700;font-size:16px;line-height:1.25;text-align:center;display:flex;align-items:center;justify-content:center;padding:0 18px}
  .title{position:absolute;left:30px;top:112px;font-size:38px;font-weight:500;color:var(--white)}
  .subtitle{position:absolute;left:30px;top:166px;font-size:22px;color:var(--white)}
  .packages{position:absolute;left:28px;top:232px;width:604px;border-collapse:collapse;border-radius:10px;overflow:hidden;font-size:10px;table-layout:fixed}
  .packages td,.packages th{height:19px;border:1px solid rgba(255,255,255,.55);text-align:center;font-weight:400;padding:0 6px}
  .packages col.label{width:184px}
  .packages thead th{background:var(--green-dark);color:var(--white);font-weight:600}
  .packages .price td{background:var(--green-light);color:var(--white)}
  .packages .section td{background:var(--plum);color:var(--white)}
  .packages .feature td{background:var(--pink-row);color:var(--ink)}
  .packages .feature:nth-child(even) td{background:var(--pink-row-alt)}
  .packages .feature td:first-child{text-align:left}
  .features{position:absolute;left:28px;top:714px;width:604px;display:flex;justify-content:space-between}
  .feature-card{width:108px;text-align:center}
  .feature-card svg{display:block;margin:0 auto;height:32px}
  .feature-box{margin-top:2px;height:68px;border-radius:10px;border:2px solid var(--white);box-shadow:0 2px 4px rgba(0,0,0,.25);color:var(--white);font-weight:700;font-size:13px;line-height:1.25;display:flex;align-items:center;justify-content:center;padding:0 16px}
  .feature-box.plum{background:var(--plum)}
  .feature-box.green{background:var(--green)}
  .cta{position:absolute;left:28px;top:830px;width:604px;height:60px;background:var(--plum);border-radius:10px;border:2px solid var(--white);box-shadow:0 2px 4px rgba(0,0,0,.25);color:var(--white);text-align:center;padding-top:6px}
  .cta-main{font-size:20px;font-weight:700}
  .cta-sub{font-size:17px}
  .contacts{position:absolute;left:30px;top:902px;width:600px;display:flex;justify-content:space-between;color:var(--plum);font-weight:700;font-size:19px}
</style>
</head>
<body>
<div class="flyer">
  <div class="sketch-bg" role="img" aria-label="Faint background sketch of technical line drawing"></div>

  <header class="header">
    <div class="brand"><span class="brand-dot"></span><span class="brand-name">corvanta</span></div>
    <div class="strap">YOUR LOCAL IT COMPANY</div>
    <div class="badge">IT support from £10pm – from a trusted provider based in Dunmarsh</div>
    <h1 class="title">Affordable IT Support Packages</h1>
    <p class="subtitle">Peace of mind for your business at competitive prices</p>
  </header>

  <table class="packages">
    <colgroup><col class="label"><col><col><col><col></colgroup>
    <thead><tr><th>IT Support Packages</th><th>Remote</th><th>Plus</th><th>Pro</th><th>Unlimited</th></tr></thead>
    <tbody>
      <tr class="price"><td>Per Server</td><td>£45pm</td><td>£85pm</td><td>£85pm</td><td>£85pm</td></tr>
      <tr class="price"><td>Per Computers</td><td>£10pm</td><td>£10pm</td><td>£13pm</td><td>£15pm</td></tr>
      <tr class="section"><td colspan="5">Support service</td></tr>
      <tr class="feature"><td>Server support</td><td>✓</td><td>✓</td><td>✓</td><td>✓</td></tr>
      <tr class="feature"><td>PC/device support</td><td>✓</td><td>✓</td><td>✓</td><td>✓</td></tr>
      <tr class="section"><td colspan="5">Server/Network callout</td></tr>
      <tr class="feature"><td>Remote support</td><td>✓</td><td>✓</td><td>✓</td><td>✓</td></tr>
      <tr class="feature"><td>Onsite callout (4hr response)</td><td>£40</td><td>✓</td><td>✓</td><td>✓</td></tr>
      <tr class="feature"><td>Hourly rate onsite</td><td>£25ph</td><td>Included</td><td>Included</td><td>Included</td></tr>
      <tr class="section"><td colspan="5">Computer/equipment/device callout</td></tr>
      <tr class="feature"><td>Remote support</td><td>✓</td><td>✓</td><td>✓</td><td>✓</td></tr>
      <tr class="feature"><td>Onsite callout (8hr response)</td><td>£40</td><td>£40</td><td>✓</td><td>✓</td></tr>
      <tr class="feature"><td>Hourly rate onsite</td><td>£25ph</td><td>£25ph</td><td>Included</td><td>Included</td></tr>
      <tr class="section"><td colspan="5">Protection/Security</td></tr>
      <tr class="feature"><td>Kivoro anti-virus (per PC)</td><td>£2</td><td>£2</td><td>£2</td><td>✓</td></tr>
      <tr class="feature"><td>Kivoro content filter (per PC)</td><td>£1.30</td><td>£1.30</td><td>£1.30</td><td>✓</td></tr>
      <tr class="feature"><td>Remote back-up (per unit, 5GB)</td><td>£1.50</td><td>£1.50</td><td>£1.50</td><td>✓</td></tr>
      <tr class="section"><td colspan="5">Monitoring</td></tr>
      <tr class="feature"><td>Daily back-up checks</td><td>✓</td><td>✓</td><td>✓</td><td>✓</td></tr>
      <tr class="feature"><td>24/7 monitoring</td><td>✓</td><td>✓</td><td>✓</td><td>✓</td></tr>
      <tr class="section"><td colspan="5">Maintenance</td></tr>
      <tr class="feature"><td>Patch management</td><td>✓</td><td>✓</td><td>✓</td><td>✓</td></tr>
      <tr class="feature"><td>Software updates</td><td>✓</td><td>✓</td><td>✓</td><td>✓</td></tr>
      <tr class="feature"><td>Security updates</td><td>✓</td><td>✓</td><td>✓</td><td>✓</td></tr>
    </tbody>
  </table>

  <section class="features">
    <div class="feature-card">
      <svg viewBox="0 0 32 32" role="img" aria-label="Desk lamp icon"><path d="M10 4h12l-3 10h-6z" fill="var(--icon)"/><rect x="15" y="14" width="2" height="12" fill="var(--icon)"/><rect x="9" y="26" width="14" height="4" rx="1" fill="var(--icon)"/></svg>
      <div class="feature-box plum">Affordable, local service</div>
    </div>
    <div class="feature-card">
      <svg viewBox="0 0 32 32"><rect x="11" y="3" width="10" height="27" rx="2" fill="var(--icon)"/><rect x="13" y="7" width="6" height="7" fill="#9aa"/></svg>
      <div class="feature-box green">4 hour callout</div>
    </div>
    <div class="feature-card">
      <svg viewBox="0 0 32 32"><path d="M4 14a17 17 0 0 1 24 0M8 18a11 11 0 0 1 16 0M12 22a5 5 0 0 1 8 0" fill="none" stroke="var(--green)" stroke-width="3"/><rect x="13" y="25" width="6" height="6" rx="1" fill="var(--icon)"/></svg>
      <div class="feature-box plum">Remote support</div>
    </div>
    <div class="feature-card">
      <svg viewBox="0 0 32 32"><circle cx="16" cy="16" r="14" fill="var(--icon)"/><circle cx="16" cy="16" r="11" fill="#555"/><path d="M16 8v8l5 3" stroke="#ddd" stroke-width="2" fill="none"/></svg>
      <div class="feature-box green">24/7 monitoring</div>
    </div>
    <div class="feature-card">
      <svg viewBox="0 0 32 32"><rect x="5" y="3" width="22" height="17" rx="1" fill="var(--icon)"/><rect x="8" y="6" width="16" height="11" fill="#8a9"/><rect x="12" y="22" width="18" height="8" fill="var(--icon)"/></svg>
      <div class="feature-box plum">Server / PC builds from £250</div>
    </div>
  </section>

  <div class="cta">
    <div class="cta-main">Protect your business and keep downtime costs at bay</div>
    <div class="cta-sub">Call, email or live chat with us on our website today!</div>
  </div>

  <footer class="contacts">
    <span>01632 960 418</span>
    <span>info@corvanta.co.uk</span>
    <span>www.corvanta.co.uk</span>
  </footer>
</div>
</body>
</html>
```